Technology Service Provider Needs a Business Card

Need a business card that includes the following:
_Name of Individual
_Address
_Phone Number(s)
_Email Address
_Web Page Address
_Tagline or Description of Business
_Logo
_List of Services or Products: IT Managed Services & Consulting

Both portrait or landscape layouts are welcomed.

Full bleed on one side is required.

Files delivered must be able to self-edit in future.

See attachments: Options 1 and 2 are examples of cards we like.
- pGLM logo is our current logo

Industry/Entity Type

Business

Requirements
Nice to have
• Full bleed front side color

```html
<!DOCTYPE html>
<html lang="en">
<head>
<meta charset="utf-8">
<title>PGLM Business Card</title>
<link rel="stylesheet" href="https://fonts.googleapis.com/css2?family=Questrial&display=swap">
<style>
  :root {
    --stage: #e4e4e4;
    --brand-blue: #3a5bb5;
    --card-white: #fbfbfb;
    --ink: #2e2e2e;
    --accent-green: #7dc23f;
    --white: #ffffff;
  }
  * { box-sizing: border-box; margin: 0; padding: 0; }
  html, body {
    width: 1200px; height: 949px; overflow: hidden;
    background: var(--stage);
    font-family: "Questrial", "Century Gothic", sans-serif;
  }
  .canvas { position: relative; width: 1200px; height: 949px; }

  .card {
    position: absolute;
    width: 560px; height: 320px;
    border-radius: 22px;
    box-shadow: 0 10px 24px rgba(0,0,0,0.18);
  }

  /* Front side: full bleed colour */
  .card--front {
    left: 130px; top: 90px;
    background: var(--brand-blue);
    display: flex; flex-direction: column; align-items: center; justify-content: center;
    color: var(--white);
  }
  .card--front .brand-name {
    font-size: 84px; line-height: 1; letter-spacing: 4px;
  }
  .card--front .brand-descriptor {
    margin-top: 12px; font-size: 17px; letter-spacing: 2.5px;
  }

  /* Back side: contact details */
  .card--back {
    left: 510px; top: 520px;
    background: var(--card-white);
    color: var(--ink);
  }
  .identity {
    position: absolute; left: 36px; top: 30px;
    display: flex; align-items: center; gap: 14px;
  }
  .identity .person-name { font-size: 21px; letter-spacing: 1px; text-transform: uppercase; }
  .identity .person-role { font-size: 19px; letter-spacing: 0.5px; }
  .identity-rule {
    position: absolute; left: 36px; top: 94px;
    width: 300px; height: 3px; background: var(--accent-green);
  }
  .contact-list {
    position: absolute; left: 36px; top: 118px;
    list-style: none; display: flex; flex-direction: column; gap: 12px;
  }
  .contact-item { display: flex; align-items: center; gap: 14px; font-size: 16px; line-height: 1.3; }
  .icon { width: 34px; height: 34px; flex: none; }

  .brand-lockup {
    position: absolute; right: 34px; bottom: 36px; width: 220px;
    text-align: center; color: var(--brand-blue);
  }
  .brand-lockup .brand-name { font-size: 68px; line-height: 1; letter-spacing: 3px; }
  .brand-lockup .brand-tagline { font-size: 14px; letter-spacing: 1px; margin-top: 8px; }
</style>
</head>
<body>
<main class="canvas">

  <section class="card card--front" aria-label="Card front">
    <div class="brand-name">PGLM</div>
    <div class="brand-descriptor">Managed Services Provider</div>
  </section>

  <section class="card card--back" aria-label="Card back">
    <div class="identity">
      <svg class="icon" viewBox="0 0 34 34" aria-hidden="true">
        <circle cx="17" cy="17" r="17" fill="var(--brand-blue)"/>
        <circle cx="17" cy="13" r="5" fill="var(--white)"/>
        <path d="M8 26c1-5 5-7 9-7s8 2 9 7z" fill="var(--white)"/>
      </svg>
      <div>
        <div class="person-name">Daniel Morrow</div>
        <div class="person-role">Managing Director</div>
      </div>
    </div>
    <div class="identity-rule"></div>

    <ul class="contact-list">
      <li class="contact-item">
        <svg class="icon" viewBox="0 0 34 34" aria-hidden="true">
          <circle cx="17" cy="17" r="17" fill="var(--accent-green)"/>
          <rect x="12" y="8" width="10" height="18" rx="2" fill="none" stroke="var(--white)" stroke-width="2"/>
          <circle cx="17" cy="22.5" r="1.2" fill="var(--white)"/>
        </svg>
        <span>012 555 0148<br>012 555 0149</span>
      </li>
      <li class="contact-item">
        <svg class="icon" viewBox="0 0 34 34" aria-hidden="true">
          <circle cx="17" cy="17" r="17" fill="var(--accent-green)"/>
          <rect x="8" y="9" width="18" height="12" rx="1.5" fill="none" stroke="var(--white)" stroke-width="2"/>
          <path d="M13 25h8M17 21v4" stroke="var(--white)" stroke-width="2"/>
        </svg>
        <span>dmorrow@mail.com<br>pglmservices.com</span>
      </li>
      <li class="contact-item">
        <svg class="icon" viewBox="0 0 34 34" aria-hidden="true">
          <circle cx="17" cy="17" r="17" fill="var(--accent-green)"/>
          <path d="M17 27s-7-7.5-7-12a7 7 0 0 1 14 0c0 4.5-7 12-7 12z" fill="var(--white)"/>
          <circle cx="17" cy="15" r="2.6" fill="var(--accent-green)"/>
        </svg>
        <span>214, 9th floor, Harbor<br>Point Road Eastvale</span>
      </li>
    </ul>

    <div class="brand-lockup">
      <div class="brand-name">PGLM</div>
      <div class="brand-tagline">Planned · Built · Supported</div>
    </div>
  </section>

</main>
</body>
</html>
```